BUSINESS CARD DESIGN

NAME- TODD MASVERIK
PHONE NUMER - 808- 451-7082
EMAIL- OFFICE@VORLINDE-GRADEWAY.COM
BACK OF CARD- SPEACIALIZES IN LAND CLEARING, FORESTRY MUCLHING AND EXCAVATION

Contact Information for Business Card

NAME- TODD MASVERIK PHONE NUMER - 808- 451-7082 EMAIL- OFFICE@VORLINDE-GRADEWAY.COM BACK OF CARD- SPEACIALIZES IN LAND CLEARING , MUCLHING AND EXCAVATION

```html
<!DOCTYPE html>
<html lang="en">
<head>
<meta charset="utf-8">
<title>Vorlinde Gradeway LLC — Business Card</title>
<link rel="stylesheet" href="https://fonts.googleapis.com/css2?family=Montserrat:wght@400;500;700&family=Inter:wght@400;500&display=swap">
<style>
  :root {
    --backdrop: #e2e2e2;
    --card-dark: #070809;
    --card-light: #ffffff;
    --ink: #111111;
    --ink-soft: #4a4a4a;
    --ink-muted: #7a7a7a;
    --rule: #c9c9c9;
    --paper: #ffffff;
  }
  * { margin: 0; padding: 0; box-sizing: border-box; }
  html, body { width: 1200px; height: 1200px; overflow: hidden; }
  body { background: var(--backdrop); position: relative; font-family: "Montserrat", sans-serif; }

  .card { position: absolute; left: 179px; width: 861px; height: 496px; }
  .card--front { top: 84px; background: var(--card-dark); color: var(--paper); }
  .card--back { top: 621px; background: var(--card-light); color: var(--ink); }

  .brand { position: absolute; display: flex; flex-direction: column; align-items: center; font-family: "Montserrat", sans-serif; font-weight: 700; text-align: center; }
  .brand__mark { width: 120px; height: 120px; border-radius: 50%; border: 3px solid currentColor; margin-bottom: 14px; }
  .brand__name { font-size: 20px; letter-spacing: 1.5px; line-height: 1.3; }
  .brand__phone { font-size: 12px; letter-spacing: 7px; margin-top: 4px; }

  .card--front .brand { left: 0; right: 0; top: 123px; }
  .tagline { position: absolute; left: 0; right: 0; top: 422px; text-align: center; font-size: 21px; font-weight: 400; letter-spacing: 1.8px; line-height: 27px; }

  .card--back .brand { left: 80px; width: 256px; top: 143px; }
  .card--back .brand__mark { width: 130px; height: 130px; }
  .divider { position: absolute; left: 359px; top: 152px; width: 1px; height: 186px; background: var(--rule); }

  .contact { position: absolute; left: 381px; top: 150px; }
  .contact__name { font-size: 30px; font-weight: 700; letter-spacing: 0.5px; line-height: 1.1; color: var(--ink); }
  .contact__role { font-size: 21px; font-weight: 500; letter-spacing: 1px; color: var(--ink-muted); margin-top: 2px; }
  .contact__address { font-family: "Inter", sans-serif; font-size: 18px; letter-spacing: 1.2px; line-height: 29px; color: var(--ink-soft); margin-top: 14px; margin-left: 2px; }
  .contact__list { list-style: none; margin-top: 10px; font-family: "Inter", sans-serif; font-size: 18px; letter-spacing: 1.2px; color: var(--ink-soft); }
  .contact__item { display: flex; align-items: center; height: 29px; }
  .contact__icon { width: 22px; height: 20px; margin-right: 14px; flex: none; }
</style>
</head>
<body>
  <section class="card card--front">
    <div class="brand">
      <div class="brand__mark"></div>
      <div class="brand__name">VORLINDE GRADEWAY<br>LLC HAWAII</div>
      <div class="brand__phone">808-451-7082</div>
    </div>
    <p class="tagline">SPEACIALIZES IN LAND CLEARING , MUCLHING<br>AND EXCAVATION</p>
  </section>

  <section class="card card--back">
    <div class="brand">
      <div class="brand__mark"></div>
      <div class="brand__name">VORLINDE GRADEWAY<br>LLC HAWAII</div>
      <div class="brand__phone">808-451-7082</div>
    </div>
    <div class="divider"></div>
    <div class="contact">
      <h1 class="contact__name">TODD MASVERIK</h1>
      <p class="contact__role">DIRECTOR</p>
      <p class="contact__address">123 Anywhere St.<br>Any City, ST 12345</p>
      <ul class="contact__list">
        <li class="contact__item">
          <svg class="contact__icon" viewBox="0 0 24 24" aria-hidden="true"><path d="M6.6 2.5l3 3.6-1.9 2.2c1.2 2.6 3.3 4.7 5.9 5.9l2.2-1.9 3.6 3-1.8 3.2C11 18 6 13 4.5 4.3z" fill="none" stroke="#222" stroke-width="1.8" stroke-linejoin="round"/></svg>
          <span>808- 451-7082</span>
        </li>
        <li class="contact__item">
          <svg class="contact__icon" viewBox="0 0 24 18" aria-hidden="true"><rect x="1" y="1.5" width="22" height="15" fill="none" stroke="#222" stroke-width="1.8"/><path d="M1 1.5l11 9 11-9" fill="none" stroke="#222" stroke-width="1.8"/></svg>
          <span>OFFICE@VORLINDE-GRADEWAY.COM</span>
        </li>
      </ul>
    </div>
  </section>
</body>
</html>
```